Natural and organic skincare brand needs label design!

I need labels designed for my natural and organic skincare brand lumavale. The front of the bottles must contain the logo (image attached) and the following words: Formulated by a Naturopath; Anti-aging therapy; Organic Facial Oil; with CoEnzyme Q10 and Rosehip Seed Oil; 100ml e3.38fl.oz. Colours I would like used include black/white/grey/silver and aqua. I also like the grey woodgrain used on my draft website (check out www.lumavale-skin.com.au). The logo should be silver foil (shiny).The final design should be simple and communicate nature and sophistication. Some designs I like are found in the attachments. I intend to use black or white bottles.

Target Market(s)

women aged 30-50 interested in natural products

Industry/Entity Type

Skin Care Product

Font styles to use
Serif
Sans Serif
Decorative
Script
Other font styles liked:
• Any

Requirements
Must have
• Dimensions: 62mm (w) x 75mm (H) (front label only)
• Must contain the logo (image attached). The logo should be silver foil (shiny). and the following words are to be included on the label:
• Formulated by a Naturopath;
• Anti-aging Therapy;
• Organic Facial Oil;
• with CoEnzyme Q10 and Rosehip Seed Oil;
• 100ml e3.38fl.oz.
Nice to have
• Colours I would like used include black/white/grey/silver and aqua (turquoise). But I am also open to suggestion. I also like the grey woodgrain used on my draft website (check out www.lumavale-skin.com.au)

```html
<!DOCTYPE html>
<html lang="en">
<head>
<meta charset="utf-8">
<title>lumavale – Organic Facial Oil Label</title>
<link rel="stylesheet" href="https://fonts.googleapis.com/css2?family=Questrial&display=swap">
<style>
  :root {
    --page: #ffffff;
    --label-black: #000000;
    --frame-grey: #5a616d;
    --slate: #535a66;
    --slate-ring: #4b525d;
    --leaf-dark: #202226;
    --leaf-mid: #3a3c40;
    --text-white: #ffffff;
    --volume-grey: #3d4148;
    --dimension-grey: #7a7a7a;
  }
  * { margin: 0; padding: 0; box-sizing: border-box; }
  html, body {
    width: 1153px;
    height: 1200px;
    overflow: hidden;
    background: var(--page);
    font-family: "Questrial", "Helvetica Neue", Arial, sans-serif;
  }
  .canvas { position: relative; width: 1153px; height: 1200px; }

  .label {
    position: absolute;
    left: 19px; top: 0;
    width: 908px; height: 1119px;
    background: var(--label-black);
  }
  .label__frame {
    position: absolute;
    border: 3px solid var(--frame-grey);
  }
  .label__frame--outer { inset: 21px; }
  .label__frame--inner { inset: 34px; }

  .label__pattern {
    position: absolute;
    inset: 40px;
    background:
      radial-gradient(ellipse at 30% 20%, var(--leaf-mid) 0%, transparent 60%),
      radial-gradient(ellipse at 80% 75%, var(--leaf-mid) 0%, transparent 55%),
      linear-gradient(160deg, var(--leaf-dark), #141517 50%, var(--leaf-dark));
  }

  .brand-seal {
    position: absolute;
    left: 228px; top: 182px;
    width: 434px; height: 434px;
  }
  .brand-seal__name {
    position: absolute;
    inset: 0;
    display: flex;
    align-items: center;
    justify-content: center;
    color: var(--text-white);
    font-size: 58px;
    letter-spacing: 5px;
  }

  .claims {
    position: absolute;
    left: 114px; top: 701px;
    width: 661px; height: 265px;
    background: var(--slate);
    color: var(--text-white);
    text-align: center;
    padding-top: 28px;
  }
  .claims__title { font-size: 39px; letter-spacing: 3px; line-height: 1.2; }
  .claims__ingredients { font-size: 19px; margin-top: 6px; }
  .claims__benefit { font-size: 39px; letter-spacing: 3px; line-height: 1.2; margin-top: 10px; }
  .claims__credit { font-size: 28px; letter-spacing: 1px; margin-top: 6px; }

  .volume {
    position: absolute;
    left: 0; right: 0; top: 998px;
    text-align: center;
    font-size: 31px;
    letter-spacing: 2px;
    color: var(--volume-grey);
  }

  .dimension {
    position: absolute;
    font-size: 43px;
    font-style: italic;
    color: var(--dimension-grey);
  }
  .dimension--height { left: 988px; top: 535px; }
  .dimension--width { left: 380px; top: 1148px; }
</style>
</head>
<body>
<div class="canvas">
  <div class="label">
    <div class="label__pattern" role="img" aria-label="Repeating pattern of grey leaves on black"></div>
    <div class="label__frame label__frame--outer"></div>
    <div class="label__frame label__frame--inner"></div>

    <div class="brand-seal">
      <svg width="434" height="434" viewBox="0 0 434 434" aria-hidden="true">
        <circle cx="217" cy="217" r="217" fill="var(--slate-ring)"/>
        <circle cx="217" cy="217" r="190" fill="var(--slate)" stroke="var(--text-white)" stroke-width="3"/>
      </svg>
      <div class="brand-seal__name">lumavale</div>
    </div>

    <div class="claims">
      <p class="claims__title">ORGANIC FACIAL OIL</p>
      <p class="claims__ingredients">With CoEnzyme Q10 and Rosehip Seed Oil</p>
      <p class="claims__benefit">ANTI-AGING THERAPY</p>
      <p class="claims__credit">Formulated by a NATUROPATH</p>
    </div>

    <p class="volume">100ml e3.38fl.oz</p>
  </div>

  <p class="dimension dimension--height">75 mm</p>
  <p class="dimension dimension--width">62 mm</p>
</div>
</body>
</html>
```